Letter Head Design

I need a letter head design based on my company logo that I attached.
Include phone number: (403)582-4316
Address: 347 14th Avenue NE, Calgary, Alberta, Canada, T3K 4R8

Industry/Entity Type

It Company

```html
<!DOCTYPE html>
<html lang="en">
<head>
<meta charset="utf-8">
<title>BrightNest Letterhead</title>
<link rel="stylesheet" href="https://fonts.googleapis.com/css2?family=Open+Sans:wght@400;600&family=Tinos&display=swap">
<style>
  :root {
    --backdrop: #f1f1f1;
    --paper: #ffffff;
    --ink: #2b2b2b;
    --brand-blue: #1a4fa0;
    --band-blue: #1c3f8f;
    --tab-light: #3f7fd0;
    --tab-dark: #1e4c9c;
    --signature-tone: #d9d9d9;
  }
  * { box-sizing: border-box; margin: 0; padding: 0; }
  html, body { width: 1200px; height: 560px; overflow: hidden; background: var(--backdrop); }
  .canvas { position: relative; width: 1200px; height: 560px; }
  .letterhead {
    position: absolute; left: 430px; top: 16px; width: 340px; height: 528px;
    background: var(--paper); box-shadow: 0 2px 8px rgba(0,0,0,.12); overflow: hidden;
  }
  .brand-header {
    position: absolute; top: 40px; left: 0; width: 100%;
    display: flex; justify-content: center; align-items: center; gap: 6px;
  }
  .brand-square { width: 14px; height: 14px; background: var(--brand-blue); }
  .brand-name {
    font-family: "Open Sans", sans-serif; font-weight: 600; font-size: 15px;
    color: var(--brand-blue); letter-spacing: -.2px;
  }
  .letter-body {
    position: absolute; top: 134px; left: 53px; right: 28px;
    font-family: "Tinos", serif; font-size: 5.6px; line-height: 9.2px; color: var(--ink);
  }
  .salutation { margin-bottom: 9px; }
  .letter-body p { margin-bottom: 17px; }
  .closing { margin-top: -4px; }
  .signature {
    display: block; width: 62px; height: 14px; margin: 6px 0 4px;
    background: var(--signature-tone); border-radius: 2px;
  }
  .footer-band { position: absolute; left: 0; bottom: 0; width: 340px; height: 42px; }
  .contact {
    position: absolute; bottom: 8px; left: 20px; display: flex; gap: 12px; align-items: center;
    font-family: "Open Sans", sans-serif; font-size: 5.6px; color: #fff;
  }
  .contact-item { display: flex; align-items: center; gap: 5px; }
  .contact-item svg { width: 6px; height: 6px; fill: #fff; }
  .footer-brand {
    position: absolute; right: 12px; bottom: 30px; display: flex; align-items: center; gap: 4px;
    font-family: "Open Sans", sans-serif; font-weight: 600; font-size: 7px; color: #fff;
  }
  .footer-brand .brand-square { width: 9px; height: 9px; background: #fff; }
</style>
</head>
<body>
<div class="canvas">
  <div class="letterhead">
    <div class="brand-header">
      <span class="brand-square"></span>
      <span class="brand-name">BrightNest</span>
    </div>

    <div class="letter-body">
      <div class="salutation">Dear Marco,<br><br>Managing Director</div>
      <p>This is not real copy. This is Greek. And nobody's supposed to be able to understand Greek. Hence the phrase, "Hey, man, it's all Greek to me" which means "I don't understand it." So if you're reading along, and you notice that this copy isn't making any sense, that's perfectly alright. Because it's not important that you get the meaning of the copy. After all, it's Greek. And nobody's supposed to be able to understand Greek.</p>
      <p>This is Greek. And nobody's supposed to be able to understand Greek. Hence the phrase, "Hey, man, it's all Greek to me" which means "I don't understand it." So if you're reading along, and you notice that this copy isn't making any sense, that's perfectly alright. Because it's not important that you get the meaning of the copy. After all, it's Greek. And nobody's supposed to be able to understand Greek. Hence the phrase, "Hey, man, it's all Greek." This is not real copy. This is Greek. And nobody's supposed to be able to understand Greek. Hence the phrase, "Hey, man, it's all Greek to me" which means "I don't understand it." So if you're reading along, and you notice that this copy isn't making any sense, that's perfectly alright. Because it's not important that you get the meaning.</p>
      <p>And nobody's supposed to be able to understand Greek. Hence the phrase, "Hey, man, it's all Greek to me" which means "I don't understand it." So if you're reading along, and you notice that this copy isn't making any sense, that's perfectly alright.</p>
      <div class="closing">
        Sincerly
        <span class="signature" role="img" aria-label="Handwritten signature"></span>
        R. Hale
      </div>
    </div>

    <svg class="footer-band" viewBox="0 0 340 42" aria-hidden="true">
      <defs>
        <linearGradient id="tab-gradient" x1="0" y1="0" x2="1" y2="0">
          <stop offset="0" stop-color="var(--tab-dark)"/>
          <stop offset="1" stop-color="var(--tab-light)"/>
        </linearGradient>
      </defs>
      <rect x="0" y="18" width="340" height="24" fill="var(--band-blue)"/>
      <polygon points="268,2 340,2 340,18 252,18" fill="url(#tab-gradient)"/>
    </svg>

    <div class="footer-brand">
      <span class="brand-square"></span>
      <span>BrightNest</span>
    </div>

    <div class="contact">
      <span class="contact-item">
        <svg viewBox="0 0 24 24"><path d="M6.6 10.8a15.1 15.1 0 0 0 6.6 6.6l2.2-2.2a1 1 0 0 1 1-.25 11.4 11.4 0 0 0 3.6.57 1 1 0 0 1 1 1V20a1 1 0 0 1-1 1A17 17 0 0 1 3 4a1 1 0 0 1 1-1h3.5a1 1 0 0 1 1 1c0 1.25.2 2.45.57 3.57a1 1 0 0 1-.25 1z"/></svg>
        (403)582-4316
      </span>
      <span class="contact-item">
        <svg viewBox="0 0 24 24"><path d="M12 2a7 7 0 0 0-7 7c0 5.25 7 13 7 13s7-7.75 7-13a7 7 0 0 0-7-7zm0 9.5A2.5 2.5 0 1 1 12 6.5a2.5 2.5 0 0 1 0 5z"/></svg>
        347 14th Avenue NE, Calgary, Alberta, Canada, T3K 4R8
      </span>
    </div>
  </div>
</div>
</body>
</html>
```